Soziale Betreuung für Senioren, die von Herzen kommt!
Zielgruppe
Betreuung von Senioren (keine Pflege) mit den 3 Schwerpunkten „Miteinander reden“, „im Alltag unterstützen“ und „Freizeit gestalten“
Aufgabenstellung
Entwicklung eines Flyers als Hauptwerbemedium, das Interesse bei den Senioren weckt (große
Buchstaben für den Teil, der sich an die Senioren richtet) und auch die Angehörigen überzeugt.
DIN A4 Lang 6-seitig Wickelfalz.

```html
<!DOCTYPE html>
<html lang="de">
<head>
<meta charset="utf-8">
<title>Flyer – Soziale Betreuung für Senioren</title>
<link href="https://fonts.googleapis.com/css2?family=Noto+Serif:ital,wght@0,400;0,700;1,400;1,700&family=Caveat&display=swap" rel="stylesheet">
<style>
  :root{
    --cream:#f9e9c6;
    --red:#e0241c;
    --ink:#1b1b1b;
    --stage:#dcdcdc;
  }
  *{box-sizing:border-box;margin:0;padding:0}
  html,body{width:1200px;height:800px;overflow:hidden;background:var(--stage)}
  body{font-family:"Noto Serif",Georgia,serif;color:var(--ink);position:relative}
  .spread{position:absolute;top:195px;width:580px;height:410px;display:grid;grid-template-columns:repeat(3,1fr);background:var(--cream);box-shadow:0 4px 14px rgba(0,0,0,.25)}
  .spread--outside{left:13px}
  .spread--inside{left:607px}
  .panel{position:relative;overflow:hidden;padding:10px 11px;border-right:1px solid rgba(0,0,0,.08)}
  .panel:last-child{border-right:none}
  .photo{display:block;width:100%}
  .heading{font-weight:700;letter-spacing:.08em;border-bottom:2px solid var(--red);display:inline-block;line-height:1.25;padding-bottom:1px}
  .red{color:var(--red)}
  .tick{width:13px;height:13px;vertical-align:-2px;margin-right:3px}
  .brand{display:flex;align-items:center;gap:5px;font-weight:700;letter-spacing:.08em;color:var(--red)}
  .brand__dot{width:10px;height:10px;border-radius:50%;background:var(--red);flex:none}

  /* Angebot */
  .offer__photo{height:135px;background:linear-gradient(160deg,#a7abab,#7b8081 60%,#9aa4ad)}
  .offer__title{font-size:17px;margin-top:8px;font-style:italic}
  .offer__lead{font-size:7.5px;font-weight:700;font-style:italic;margin:5px 0 4px}
  .offer p{font-size:7.3px;font-style:italic;line-height:1.35;margin-bottom:4px;letter-spacing:.02em}
  .offer p.offer__sign{font-family:"Caveat",cursive;font-size:15px;font-style:normal;letter-spacing:0;margin-top:2px}

  /* Kontakt */
  .contact{display:flex;flex-direction:column;align-items:center}
  .contact .brand{font-size:15px;margin:48px 0 52px}
  .contact__title{font-size:20px;letter-spacing:.12em}
  .contact__list{list-style:none;margin-top:18px;width:100%}
  .contact__list li{display:flex;gap:7px;align-items:flex-start;font-size:7.6px;letter-spacing:.06em;line-height:1.3;margin-bottom:11px}
  .contact__list svg{width:14px;height:14px;flex:none}

  /* Titelseite */
  .cover{padding:0}
  .cover__band{position:absolute;left:0;width:100%}
  .cover__title{position:absolute;top:16px;left:10px;right:8px}
  .cover__title h1{font-size:15.5px;font-weight:400;letter-spacing:.06em;white-space:nowrap}
  .cover__sub{font-size:11px;letter-spacing:.1em;text-align:right;margin-top:4px}
  .cover__heart-line{display:flex;align-items:center;justify-content:space-between;font-size:11px;letter-spacing:.1em;margin-top:6px}
  .cover__heart{width:36px;height:30px;border-radius:8px;background:radial-gradient(circle at 40% 40%,#ef4a42,var(--red) 70%)}
  .cover__photo{position:absolute;top:128px;left:0;width:100%;height:115px;background:linear-gradient(120deg,#e6e6e6,#bdbdbd 45%,#c9a98a 70%,#e0e0e0)}
  .cover__list{position:absolute;top:262px;left:12px;list-style:none}
  .cover__list li{font-size:12px;letter-spacing:.1em;margin-bottom:8px;white-space:nowrap}
  .cover__list .tick{width:16px;height:16px}
  .cover .brand{position:absolute;bottom:20px;right:12px;font-size:10px}

  /* Innenseiten */
  .info h2{font-size:9.5px;margin-bottom:6px}
  .info h3{font-size:7.5px;color:var(--red);letter-spacing:.06em;margin-top:7px}
  .info p{font-size:7.2px;line-height:1.35;letter-spacing:.04em}
  .service h2{font-size:11px;margin-bottom:4px}
  .service p{font-size:7.6px;line-height:1.38;letter-spacing:.05em;margin-bottom:3px}
  .service .photo{height:62px;margin:5px 0}
  .photo--rabbits{background:linear-gradient(135deg,#8b7a5c,#c9c2b4 50%,#b23a36)}
  .photo--swing{background:linear-gradient(135deg,#b66b2d,#d7a456 45%,#2f3e5a)}
  .photo--trip{background:linear-gradient(135deg,#3f6d40,#a9c8e6 50%,#cdb58c)}
  .service .brand{font-size:8px;margin-top:6px}
  .costs p{font-size:6.9px}
</style>
</head>
<body>

<section class="spread spread--outside" aria-label="Außenseite">
  <article class="panel offer">
    <div class="photo offer__photo" role="img" aria-label="Porträtfoto der Betreuerin"></div>
    <h2 class="heading offer__title">Mein Angebot</h2>
    <p class="offer__lead">Was ist eigentlich soziale Betreuung?</p>
    <p>Lieber Interessent,</p>
    <p>es freut mich, dass Sie sich Zeit für dieses Informationsblatt nehmen.</p>
    <p>In meiner Dienstleistung geht es um „soziale Betreuung“, die dazu beitragen soll, den Alltag zu strukturieren, zu begleiten und mehr Lebensfreude zu gewinnen.</p>
    <p>Ich, Helga Sommerfeld, möchte Ihnen in dieser Informationsschrift mehr darüber erzählen.</p>
    <p>Es grüßt Sie herzlich Ihre</p>
    <p class="offer__sign">H.Sommerfeld</p>
  </article>

  <article class="panel contact">
    <div class="brand"><span class="brand__dot"></span>Herzenszeit</div>
    <h2 class="heading contact__title">Kontakt</h2>
    <ul class="contact__list">
      <li><svg viewBox="0 0 16 16" fill="none" stroke="#e0241c" stroke-width="1.2"><rect x="1.5" y="3.5" width="13" height="9"/><path d="M1.5 3.5l6.5 5 6.5-5"/></svg><span>Helga Sommerfeld<br>Lindenweg 8<br>59000 Musterstadt</span></li>
      <li><svg viewBox="0 0 16 16" fill="none" stroke="#e0241c" stroke-width="1.2"><circle cx="8" cy="8" r="6.5"/><path d="M5.5 5c0 3 2.5 5.5 5 5.5l.8-1.3-1.6-1-1 .8c-.9-.4-1.8-1.3-2.2-2.2l.8-1-1-1.6z"/></svg><span>01234 / 56 78 90</span></li>
      <li><svg viewBox="0 0 16 16" fill="none" stroke="#e0241c" stroke-width="1.2"><rect x="4.5" y="1.5" width="7" height="13" rx="1"/><path d="M6.5 11.5h3M6 4h4"/></svg><span>0170 / 12 34 56 78</span></li>
      <li><svg viewBox="0 0 16 16" fill="none" stroke="#e0241c" stroke-width="1.2"><circle cx="8" cy="8" r="2.5"/><path d="M10.5 8v1.2a1.8 1.8 0 003.5 0V8A6 6 0 108 14h2.5"/></svg><span>info@betreuung-lindenweg.de</span></li>
      <li><svg viewBox="0 0 16 16" fill="none" stroke="#e0241c" stroke-width="1.2"><circle cx="8" cy="8" r="6.5"/><ellipse cx="8" cy="8" rx="3" ry="6.5"/><path d="M1.5 8h13M2.5 4.8h11M2.5 11.2h11"/></svg><span>www.betreuung-lindenweg.de</span></li>
    </ul>
  </article>

  <article class="panel cover">
    <svg class="cover__band" style="top:0" width="194" height="12" viewBox="0 0 194 12" preserveAspectRatio="none"><path d="M0 0H194V4Q97 12 0 3Z" fill="#e0241c"/></svg>
    <div class="cover__title">
      <h1>Soziale Betreuung</h1>
      <p class="cover__sub">für Senioren,</p>
      <p class="cover__heart-line"><span>die von</span>
        <span class="cover__heart" role="img" aria-label="Illustration: rotes Herz"></span>
        <span>kommt!</span></p>
    </div>
    <div class="cover__photo" role="img" aria-label="Foto: eine junge Hand hält eine ältere Hand"></div>
    <svg class="cover__band" style="top:120px" width="194" height="20" viewBox="0 0 194 20" preserveAspectRatio="none"><path d="M0 0Q97 18 194 10V14Q97 22 0 4Z" fill="#e0241c"/></svg>
    <svg class="cover__band" style="top:236px" width="194" height="20" viewBox="0 0 194 20" preserveAspectRatio="none"><path d="M0 4Q97 -2 194 14V18Q97 2 0 8Z" fill="#e0241c"/></svg>
    <ul class="cover__list">
      <li><svg class="tick" viewBox="0 0 16 16"><path d="M1 9l4 5L15 1" fill="none" stroke="#e0241c" stroke-width="2"/></svg>Miteinander reden</li>
      <li><svg class="tick" viewBox="0 0 16 16"><path d="M1 9l4 5L15 1" fill="none" stroke="#e0241c" stroke-width="2"/></svg>Im Alltag unterstützen</li>
      <li><svg class="tick" viewBox="0 0 16 16"><path d="M1 9l4 5L15 1" fill="none" stroke="#e0241c" stroke-width="2"/></svg>Freizeit gestalten</li>
    </ul>
    <div class="brand"><span class="brand__dot"></span>Herzenszeit</div>
    <svg class="cover__band" style="bottom:0" width="194" height="12" viewBox="0 0 194 12" preserveAspectRatio="none"><path d="M0 2Q97 10 194 8V12H0Z" fill="#e0241c"/></svg>
  </article>
</section>

<section class="spread spread--inside" aria-label="Innenseite">
  <article class="panel info">
    <h2 class="heading">Infos für die Angehörigen</h2>
    <p>Ich möchte Sie gern überzeugen, dass meine Hilfe von Senioren dankbar angenommen wird.</p>
    <h3>Weniger Stress für alle</h3>
    <p>Als Angehöriger ist man oft vor besondere Herausforderungen gestellt. Schon ein plötzlich notwendiger Arztbesuch der Eltern/Großeltern bringt den Zeitplan ins Wanken.</p>
    <p>-Ich begleite die Senioren zum Arzt, auf Wunsch bis ins Behandlungszimmer!</p>
    <h3>Mehr Zeit für die schönen Dinge</h3>
    <p>In der täglichen Routine gerät man leicht in Streit. Während man selbst unter permanentem Zeitdruck leidet, haben Senioren häufig ein anderes Zeitempfinden.</p>
    <p>-Gewinnen Sie mehr gemeinsame Zeit für die schönen Dinge miteinander!</p>
    <h3>Unterstützung durch eine weitere Bezugsperson</h3>
    <p>Wie empfinden die Senioren die Unterstützung eines Dritten?</p>
    <p>-Der neue Kontakt mit weiteren Bezugspersonen wird sehr häufig als Bereicherung empfunden.</p>
    <p style="margin-top:6px">Sofern ein Angehöriger an Demenz erkrankt oder erkrankt ist, ist professionelle Hilfe, Unterstützung und Beratung gefragt. -Ich unterstütze Sie gern!</p>
    <p style="margin-top:6px">Ich bin zertifizierte Demenzbegleiterin.</p>
  </article>

  <article class="panel service">
    <h2 class="heading"><svg class="tick" viewBox="0 0 16 16"><path d="M1 9l4 5L15 1" fill="none" stroke="#e0241c" stroke-width="2"/></svg>Miteinander reden</h2>
    <p>Zeit für gemeinsame Gespräche ohne Eile, ohne Hektik. Respektvoll mit Vertrauen und Nächstenliebe.</p>
    <p class="red">Das ist mein Versprechen an Sie!</p>
    <p>Gespräche über das, was Sie bewegt, oder einfach über Dinge lachen.</p>
    <h2 class="heading" style="margin-top:6px"><svg class="tick" viewBox="0 0 16 16"><path d="M1 9l4 5L15 1" fill="none" stroke="#e0241c" stroke-width="2"/></svg>Im Alltag unterstützen</h2>
    <div class="photo photo--rabbits" role="img" aria-label="Foto: ältere Dame beim Füttern von Kaninchen"></div>
    <p>Ich unterstütze Sie gern darin, den Haushalt zusammen mit Ihnen zu organisieren. Ein schönes Gefühl, vieles noch selbst zu schaffen. Mit ein wenig Unterstützung:</p>
    <p class="red">Mehr Mobilität und Sicherheit für Sie!</p>
  </article>

  <article class="panel service">
    <div class="photo photo--swing" role="img" aria-label="Foto: Seniorenpaar an einer Schaukel im Herbstpark" style="margin-top:0"></div>
    <h2 class="heading"><svg class="tick" viewBox="0 0 16 16"><path d="M1 9l4 5L15 1" fill="none" stroke="#e0241c" stroke-width="2"/></svg>Freizeit gestalten</h2>
    <p>Schönes erleben, in einem nicht alltäglichen Umfeld. Eine Auszeit, um neue Kraft zu finden.</p>
    <p class="red">Sich auf etwas freuen, etwas vorhaben.</p>
    <p>Wenn Sie es wünschen, auch gern bei Ihnen zu Hause.</p>
    <div class="photo photo--trip" role="img" aria-label="Foto: zwei Frauen bei einem Ausflug im Grünen"></div>
    <div class="costs">
      <h2 class="heading" style="font-size:10px">Kosten:</h2>
      <p>Ich arbeite allein und ohne administrative Verwaltung oder repräsentative Geschäftsräume. Diesen Kostenvorteil gebe ich an Sie weiter. Kann in vielen Fällen über die Pflegeversicherung abgerechnet werden.</p>
      <p class="red"><b>Sprechen Sie mich gern unverbindlich an.</b></p>
    </div>
    <div class="brand"><span class="brand__dot"></span>Herzenszeit</div>
  </article>
</section>

</body>
</html>
```